Core Values - Poster

Develop a poster to display core values int he company. The design has to be align to the character and feel of the company. See our website for some inspiration. The Core Values are also listed on our website.
Our 4 core values are:
Excellence
We deliver quality services of unmatched value, constantly raising the bar on our performance, through a commitment to excellence, innovation, teamwork, ongoing learning, continuous improvement, an intense focus on client needs, and a dedication to meet those needs with a sense of urgency.
Integrity
We demonstrate honesty, fairness, openness and clear boundaries in all our interactions, behaviours and practices within the organisation and with our clients, stakeholders and the wider community. We act in accordance with our values, even when it’s difficult. We adhere to the highest ethical standards as we strive to do what is right and fair for our clients and for each other.
Sincerity
We embrace human emotions and values, and believe that sincerity is a fundamental human behaviour. We are honest with our team, and with clients in the work we do, and the way we do it. We set high expectations for ourselves to motivate hard work, and we will offer clients something that has been crafted with care, consideration and with authenticity, without cutting corners. We will put people first, and will always genuinely care.
Humility
We believe in a flat hierarchy, and that every person within the organisation is a floor sweeper. We’re not always right — we don’t have all the answers — and we know it. We’re all humans after all, and we’re not afraid to ask for help. We encourage everyone to Be Yourself, Be Open, Stay Hungry and Humble, Collaborate, Challenge, Decide and Just Do.
Everything in our Core Values need to be on the poster, which will be large (minimum 4x A4 size).
Our logo is attached in this brief - there are several colour options and layouts. Logo should be include in the poster.

```html
<!DOCTYPE html>
<html lang="en">
<head>
<meta charset="utf-8">
<title>The Bloom Practice – Core Values</title>
<link href="https://fonts.googleapis.com/css2?family=Marcellus&family=Quicksand:wght@300;500&display=swap" rel="stylesheet">
<style>
  :root {
    --bg: #3a3f1e;
    --bg-curve: #41471f;
    --bg-curve-soft: #3e4320;
    --ink: #ffffff;
    --leaf: #7ab83a;
    --hand-tone: #f4f4ee;
    --hand-shade: #e6e7dc;
  }
  * { margin: 0; padding: 0; box-sizing: border-box; }
  html, body {
    width: 848px;
    height: 1200px;
    overflow: hidden;
    background: var(--bg);
  }
  .poster {
    position: relative;
    width: 848px;
    height: 1200px;
    background: var(--bg);
    color: var(--ink);
    overflow: hidden;
  }
  .backdrop {
    position: absolute;
    inset: 0;
    width: 848px;
    height: 1200px;
  }
  .brand {
    position: absolute;
    top: 62px;
    left: 0;
    width: 100%;
    display: flex;
    justify-content: center;
    align-items: center;
    gap: 14px;
  }
  .brand-dot {
    width: 32px;
    height: 32px;
    border-radius: 50%;
    background: var(--leaf);
  }
  .brand-name {
    font-family: "Quicksand", sans-serif;
    font-weight: 500;
    font-size: 44px;
    letter-spacing: 0.5px;
    line-height: 1;
  }
  .section-label {
    position: absolute;
    top: 140px;
    left: 0;
    width: 100%;
    text-align: center;
    font-family: "Quicksand", sans-serif;
    font-weight: 300;
    font-size: 32px;
    letter-spacing: 1px;
    line-height: 1.2;
  }
  .hands {
    position: absolute;
    top: 222px;
    left: 0;
    width: 100%;
    display: flex;
    justify-content: center;
    gap: 46px;
  }
  .hand {
    width: 190px;
    height: 184px;
    border-radius: 28px;
    background: linear-gradient(180deg, var(--hand-tone), var(--hand-shade));
  }
  .values {
    position: absolute;
    top: 440px;
    left: 44px;
    width: 760px;
    display: flex;
    flex-direction: column;
    gap: 18px;
    text-align: center;
  }
  .value-title {
    font-family: "Marcellus", serif;
    font-weight: 400;
    font-size: 26px;
    letter-spacing: 1px;
    line-height: 1.2;
    margin-bottom: 6px;
  }
  .value-text {
    font-family: "Quicksand", sans-serif;
    font-weight: 300;
    font-size: 15px;
    line-height: 21px;
    text-wrap: balance;
  }
  .value-featured .value-title {
    font-size: 34px;
    margin-bottom: 10px;
  }
  .value-featured .value-text {
    font-size: 18px;
    line-height: 26px;
  }
</style>
</head>
<body>
  <main class="poster">
    <svg class="backdrop" viewBox="0 0 848 1200" aria-hidden="true">
      <path d="M520 0 C600 180 760 300 848 330 L848 0 Z" fill="var(--bg-curve)"/>
      <path d="M640 0 C690 90 780 150 848 170 L848 0 Z" fill="var(--bg-curve-soft)"/>
      <path d="M0 760 C120 900 170 1060 150 1200 L0 1200 Z" fill="var(--bg-curve-soft)"/>
      <path d="M560 1200 C640 1080 760 1010 848 990 L848 1200 Z" fill="var(--bg-curve-soft)"/>
    </svg>

    <header class="brand">
      <span class="brand-dot"></span>
      <span class="brand-name">The Bloom Practice</span>
    </header>
    <p class="section-label">CORE VALUES</p>

    <div class="hands">
      <div class="hand" role="img" aria-label="White thumbs-up hand facing right"></div>
      <div class="hand" role="img" aria-label="White thumbs-up hand facing left"></div>
    </div>

    <div class="values">
      <section class="value value-featured">
        <h1 class="value-title">EXCELLENCE</h1>
        <p class="value-text">
          We deliver quality services of unmatched value,<br>
          constantly raising the bar on our performance,<br>
          through a commitment to excellence, innovation,<br>
          teamwork, ongoing learning, continuous improvement,<br>
          an intense focus on client needs, and a dedication to<br>
          meet those needs with a sense of urgency.
        </p>
      </section>

      <section class="value">
        <h2 class="value-title">INTEGRITY</h2>
        <p class="value-text">We demonstrate honesty, fairness, openness and clear boundaries in all our interactions, behaviours and practices within the organisation and with our clients, stakeholders and the wider community. We act in accordance with our values, even when it’s difficult. We adhere to the highest ethical standards as we strive to do what is right and fair for our clients and for each other.</p>
      </section>

      <section class="value">
        <h2 class="value-title">SINCERITY</h2>
        <p class="value-text">We embrace human emotions and values, and believe that sincerity is a fundamental human behaviour. We are honest with our team, and with clients in the work we do, and the way we do it. We set high expectations for ourselves to motivate hard work, and we will offer clients something that has been crafted with care, consideration and with authenticity, without cutting corners. We will put people first, and will always genuinely care.</p>
      </section>

      <section class="value">
        <h2 class="value-title">HUMILITY</h2>
        <p class="value-text">We believe in a flat hierarchy, and that every person within the organisation is a floor sweeper. We’re not always right — we don’t have all the answers — and we know it. We’re all humans after all, and we’re not afraid to ask for help. We encourage everyone to Be Yourself, Be Open, Stay Hungry and Humble, Collaborate, Challenge, Decide and Just Do.</p>
      </section>
    </div>
  </main>
</body>
</html>
```